Veltrix4 Business Card - Health

Veltrix4 maximizes value from the health data of its clients, including doctors, HMOs, and patients. I have attached the Veltrix4 logo as an ai and eps file.
Target Market(s)
Health, HMO, Healthcare, Data, Big Data, Data Analytics
Industry/Entity Type
Business
Requirements
Must have
- At least one side should have some white on it so that we can write on it.

```html
<!DOCTYPE html>
<html lang="en">
<head>
<meta charset="utf-8">
<title>Veltrix4 Business Card</title>
<link href="https://fonts.googleapis.com/css2?family=Nunito+Sans:wght@300;400;700;800&display=swap" rel="stylesheet">
<style>
  :root {
    --backdrop: #7a5640;
    --card-white: #ffffff;
    --card-dark: #2b2b2b;
    --blue-light: #2f93d6;
    --blue-deep: #1e60b3;
    --text-light: #ffffff;
  }
  * { box-sizing: border-box; margin: 0; padding: 0; }
  html, body {
    width: 1200px; height: 1000px; overflow: hidden;
    background: var(--backdrop);
    font-family: "Nunito Sans", Arial, sans-serif;
  }
  .canvas { position: relative; width: 1200px; height: 1000px; }
  .card {
    position: absolute; left: 265px; width: 666px; height: 397px;
    box-shadow: 0 4px 10px rgba(0,0,0,0.35);
    overflow: hidden;
  }
  .card-front { top: 73px; background: var(--card-white); }
  .card-back { top: 532px; background: var(--card-dark); }
  .front-panel { position: absolute; left: 0; top: 0; width: 666px; height: 397px; }
  .contact {
    position: absolute; left: 38px; top: 72px; color: var(--text-light);
  }
  .contact-name { font-size: 25px; font-weight: 800; line-height: 1.1; }
  .contact-role { font-size: 19px; font-weight: 400; margin-top: 3px; }
  .contact-address { font-size: 19px; line-height: 24px; margin-top: 37px; }
  .contact-list { list-style: none; margin-top: 17px; }
  .contact-list li {
    display: flex; align-items: center; gap: 9px;
    font-size: 19px; height: 29px;
  }
  .contact-list svg { width: 17px; height: 17px; flex: none; }
  .brand {
    position: absolute; left: 117px; top: 143px;
    display: flex; align-items: center; gap: 30px;
  }
  .brand-dot { width: 106px; height: 106px; border-radius: 50%; background: var(--blue-light); }
  .brand-name { font-size: 92px; font-weight: 300; color: var(--text-light); letter-spacing: -1px; }
</style>
</head>
<body>
<div class="canvas">
  <section class="card card-front">
    <svg class="front-panel" viewBox="0 0 666 397" role="img" aria-label="Blue angled panel behind the contact details">
      <defs>
        <linearGradient id="panelBlue" x1="0" y1="0" x2="1" y2="1">
          <stop offset="0" stop-color="var(--blue-light)"/>
          <stop offset="1" stop-color="var(--blue-deep)"/>
        </linearGradient>
      </defs>
      <polygon points="0,0 255,0 336,40 390,287 310,397 0,397" fill="url(#panelBlue)"/>
    </svg>
    <div class="contact">
      <h1 class="contact-name">Mara Ellison</h1>
      <p class="contact-role">Manager</p>
      <p class="contact-address">418 Harlow Ave 3rd floor<br>Brookfield, CA 94512</p>
      <ul class="contact-list">
        <li><svg viewBox="0 0 16 16"><rect x="4" y="1" width="8" height="14" rx="1.5" fill="none" stroke="#fff" stroke-width="1.5"/><rect x="6" y="3" width="4" height="5" fill="#fff"/></svg>+ 555 010 020</li>
        <li><svg viewBox="0 0 16 16"><path d="M1 6c0-2 3-3 7-3s7 1 7 3l-3 1-1-2H5L4 7z" fill="#fff"/><rect x="3" y="8" width="10" height="6" rx="1" fill="#fff"/></svg>+ 555 010 021</li>
        <li><svg viewBox="0 0 16 16"><rect x="1" y="3" width="14" height="10" fill="none" stroke="#fff" stroke-width="1.5"/><path d="M1 3l7 6 7-6" fill="none" stroke="#fff" stroke-width="1.5"/></svg>info@veltrix4.com</li>
        <li><svg viewBox="0 0 16 16"><circle cx="8" cy="8" r="6.5" fill="none" stroke="#fff" stroke-width="1.5"/><path d="M1.5 8h13M8 1.5c-3 3.5-3 9.5 0 13M8 1.5c3 3.5 3 9.5 0 13" fill="none" stroke="#fff" stroke-width="1.2"/></svg>www.veltrix4.com</li>
      </ul>
    </div>
  </section>

  <section class="card card-back">
    <div class="brand">
      <span class="brand-dot"></span>
      <span class="brand-name">Veltrix4</span>
    </div>
  </section>
</div>
</body>
</html>
```